New Website for novelty yarn producer

We need a new website for our company, Tarvek. We make highly tailored yarns for weavers worldwide. This year marks our 40th anniversary and we want to evolve our image and identity.

Our temporary website can be found at:
www.tarvekyarns.com

Our only concern in that throughout the website the protagonist must be our client, we make their creations possible and are highly adaptable both during the ideation process of the yarn as well as in the production. This is at the core of the way we do business and is summarised within the concept of FPM (Fluid Partner Method).

Industry/Entity Type

Textile

Number of Pages Required

1 page

Colors
9bcb3c

Requirements
Must have
• Fluid Partner Method (FPM) - can be found on or current website www.tarvekyarns.com

```html
<!DOCTYPE html>
<html lang="en">
<head>
<meta charset="utf-8">
<title>Tarvek Novelty Yarn Solutions</title>
<link href="https://fonts.googleapis.com/css2?family=Montserrat:wght@300;400;500;600;700&display=swap" rel="stylesheet">
<style>
:root{
  --green:#9bcb3c;
  --green-deep:#5aad48;
  --green-text:#4fa63f;
  --ink:#2b2b2b;
  --grey-panel:#eeeeee;
  --white:#ffffff;
}
*{margin:0;padding:0;box-sizing:border-box}
html,body{width:960px;height:1200px;overflow:hidden;background:var(--white)}
body{font-family:'Montserrat',sans-serif;color:var(--ink);position:relative}

.site-header{position:absolute;left:0;top:0;width:960px;height:64px;background:var(--white)}
.brand{position:absolute;left:96px;top:16px;font-size:28px;font-weight:600;letter-spacing:.5px;color:var(--ink)}
.main-nav{position:absolute;right:96px;top:25px;display:flex;gap:16px}
.main-nav a{font-size:11.5px;font-weight:400;color:var(--ink);text-decoration:none;letter-spacing:.3px;position:relative;padding:0 4px}
.main-nav a.active::after{content:"";position:absolute;left:-2px;right:-2px;top:27px;height:2px;background:var(--green)}

.hero{position:absolute;left:0;top:64px;width:960px;height:400px}
.hero-photo{position:absolute;inset:0;background:
  radial-gradient(ellipse 230px 200px at 660px 210px,#e8876a 0%,#e49375 55%,rgba(220,170,150,0) 100%),
  linear-gradient(160deg,#c8c8c8 0%,#dedede 45%,#bfb7b3 100%)}
.hero-title{position:absolute;left:96px;top:146px;width:324px;text-align:center;font-weight:700;font-size:29px;line-height:37px;letter-spacing:.5px;color:var(--white)}
.hero-title .accent{color:var(--green)}
.btn{display:flex;align-items:center;justify-content:center;font-family:'Montserrat',sans-serif;font-weight:600;font-size:13px;text-decoration:none;border-radius:2px}
.hero-cta{position:absolute;left:198px;top:227px;width:119px;height:39px;background:#f2f2f2;border:2px solid var(--green);color:var(--green)}

.why-us{position:absolute;left:0;top:496px;width:960px}
.why-us .rule{position:absolute;left:460px;top:0;width:40px;height:2px;background:var(--green)}
.why-us h2{position:absolute;left:0;width:960px;top:13px;text-align:center;font-size:24px;font-weight:700;color:var(--green)}
.pillar{position:absolute;top:68px;width:256px;text-align:center}
.pillar h3{font-size:19px;font-weight:400;letter-spacing:.5px}
.pillar p{margin-top:22px;font-size:13px;font-weight:300;line-height:24px;letter-spacing:.3px;padding:0 16px}
.pillar.one{left:96px}.pillar.two{left:352px}.pillar.three{left:608px}
.divider{position:absolute;top:106px;width:1px;height:200px;background:#d6d6d6}

.band{position:absolute;left:0;top:831px;width:960px;height:257px;display:flex}
.band-method{width:480px;height:257px;background:var(--green-deep);position:relative}
.method-name{position:absolute;left:0;width:480px;top:44px;display:flex;align-items:center;justify-content:center;gap:12px;color:var(--white);font-size:16px;font-weight:400;letter-spacing:.5px}
.method-name .dot{width:14px;height:14px;border-radius:50%;background:var(--white)}
.method-tag{position:absolute;left:0;width:480px;top:141px;text-align:center;font-size:13px;font-weight:700;color:var(--white);letter-spacing:.4px}
.method-cta{position:absolute;left:180px;top:185px;width:120px;height:40px;background:var(--white);color:var(--green-deep)}
.band-stats{width:480px;height:257px;background:var(--grey-panel);position:relative}
.stat{position:absolute;width:220px;text-align:center}
.stat .num{font-size:29px;font-weight:700;color:var(--green-text);line-height:34px}
.stat .label{font-size:13px;font-weight:400;letter-spacing:.5px;margin-top:4px}
.stat.years{left:10px;top:27px}.stat.kilos{left:250px;top:27px}.stat.brands{left:130px;top:107px}
.stats-cta{position:absolute;left:180px;top:185px;width:120px;height:40px;border:2px solid var(--green-text);color:var(--green-text)}

.site-footer{position:absolute;left:96px;top:1116px;width:768px}
.footer-name{font-size:14.5px;font-weight:400;letter-spacing:.4px}
.footer-company{font-size:11px;color:var(--green);margin-top:2px;letter-spacing:.4px}
.footer-address{font-size:11px;margin-top:4px;letter-spacing:.4px}
.copyright{position:absolute;right:0;top:22px;font-size:11px;color:var(--green);letter-spacing:.4px}
</style>
</head>
<body>
<header class="site-header">
  <div class="brand">Tarvek</div>
  <nav class="main-nav">
    <a href="#" class="active">HOME</a>
    <a href="#">ABOUT US</a>
    <a href="#">FLUID PARTNER METHOD</a>
    <a href="#">HERITAGE</a>
    <a href="#">TEAM</a>
    <a href="#">BLOG</a>
    <a href="#">CONTACT</a>
  </nav>
</header>

<section class="hero">
  <div class="hero-photo" role="img" aria-label="Photo of an orange ball of yarn resting on striped grey fabric"></div>
  <h1 class="hero-title">TAILORED WEAVING<br><span class="accent">SOLUTIONS</span></h1>
  <a href="#" class="btn hero-cta">LEARN MORE</a>
</section>

<section class="why-us">
  <div class="rule"></div>
  <h2>Why Us</h2>
  <div class="pillar one">
    <h3>Experience</h3>
    <p>Over the years the company has gained the knowledge and skills that define the superiority of our product and the rigor of our work ethic</p>
  </div>
  <div class="divider" style="left:351px"></div>
  <div class="pillar two">
    <h3>Creativity</h3>
    <p>Our belief is that the key to our clients' success is a combination of innovation, creativity and quality. We strive to adapt and re-imagine our product, implementing these principles in order to meet and exceed our clients’ demands (every time)</p>
  </div>
  <div class="divider" style="left:607px"></div>
  <div class="pillar three">
    <h3>Professionality</h3>
    <p>We are a family business at the core. Our company is run with the same values as the Marelli family: respect, determination and commitment.</p>
  </div>
</section>

<section class="band">
  <div class="band-method">
    <div class="method-name"><span class="dot"></span>FLUID PARTNER METHOD</div>
    <div class="method-tag">PRODUCTION BUILT AROUND YOU</div>
    <a href="#" class="btn method-cta">Learn More</a>
  </div>
  <div class="band-stats">
    <div class="stat years"><div class="num">40</div><div class="label">YEARS IN BUSNESS</div></div>
    <div class="stat kilos"><div class="num">2</div><div class="label">MILLION KILOGRAMS/ YR</div></div>
    <div class="stat brands"><div class="num">8</div><div class="label">BRANDS</div></div>
    <a href="#" class="btn stats-cta">Learn More</a>
  </div>
</section>

<footer class="site-footer">
  <div class="footer-name">Tarvek Novelty Yarn Solutions</div>
  <div class="footer-company">Ventora s.r.l</div>
  <div class="footer-address">Via dei Tessitori 12 - 59100 Prato - Italy</div>
  <div class="copyright">© COPYRIGHT 2018. ALL RIGHTS RESERVED.</div>
</footer>
</body>
</html>
```